1 Home page redesign for existing repair service site.

We need a refresh of our existing website that looks more 2017. We have made a mockup of the content that we want and a sample of where we want it. Nothing is set in stone, if you have better ideas of where things should go, feel free.

You can see our current site at http://www.fixoloda.gr

The colors should stay orange/black/grey.

In many of the "boxes/banners" we will need images. Feel free to find in pixel vault as we have an account.

We have made notes throughout the wireframe that we have attached on what we are looking for. Let us know if you have any questions. Thanks.

Target Market(s)

People using technology and breaking it

Industry/Entity Type

It Service

Number of Pages Required

1 page

Font styles to use
Sans Serif

Requirements
Must have
• Must have a modern, professional look and feel. Need custom graphics and icons.

```html
<!DOCTYPE html>
<html lang="en">
<head>
<meta charset="utf-8">
<title>Fixoloda – Device Repair</title>
<link href="https://fonts.googleapis.com/css2?family=Roboto:wght@300;400;500;700;900&family=Open+Sans:wght@400;600&display=swap" rel="stylesheet">
<style>
:root{
  --orange:#f7901e;
  --orange-dark:#e57c0c;
  --black:#141414;
  --ink:#222;
  --grey-dark:#333;
  --grey-mid:#555;
  --grey-light:#eeeeee;
  --grey-pale:#f6f6f6;
  --white:#fff;
}
*{box-sizing:border-box;margin:0;padding:0}
html,body{width:1200px;height:3309px;overflow:hidden}
body{font-family:"Roboto",Arial,sans-serif;color:var(--ink);background:var(--white);position:relative}
a{color:inherit;text-decoration:none}
.wrap{width:880px;margin:0 auto;position:relative}

/* top bar */
.topbar{height:31px;background:var(--black);color:#ddd;font-size:11px}
.topbar .wrap{height:31px;display:flex;align-items:center;justify-content:space-between}
.quick-links{background:#2b2b2b;height:31px;width:175px;display:flex;align-items:center;justify-content:center;gap:16px;font-weight:700;letter-spacing:.5px;color:#fff}
.top-right{display:flex;align-items:center;gap:9px}
.lang b{color:#fff}
.social-dot{width:12px;height:12px;border-radius:50%;background:#bbb}

/* header */
.header{height:79px;background:var(--white);border-bottom:1px solid #ddd}
.header .wrap{height:79px;display:flex;align-items:center}
.brand{display:flex;align-items:center;gap:10px;font-size:31px;font-weight:700;color:var(--ink);width:248px}
.brand-mark{width:30px;height:30px;background:var(--orange);border-radius:4px}
.nav{display:flex;height:79px}
.nav a{display:flex;align-items:center;padding:0 22px;font-size:16px;border-left:1px solid #e3e3e3}
.nav a:last-child{border-right:1px solid #e3e3e3}
.call{margin-left:auto;display:flex;align-items:center;gap:10px}
.call-icon{width:34px;height:34px;border:2px solid var(--orange);border-radius:50%;display:flex;align-items:center;justify-content:center}
.call small{display:block;color:#e33;font-size:13px}
.call strong{font-size:19px;font-weight:700}
.chat-btn{margin-left:34px;border:2px solid var(--ink);border-radius:6px;padding:6px 9px;font-size:16px;font-weight:700}

/* hero */
.hero{height:430px;background:radial-gradient(ellipse at 65% 35%,#9a9a9a 0%,#5d5d5d 35%,#2c2c2c 75%,#1d1d1d 100%);position:relative}
.play{position:absolute;left:568px;top:283px;width:64px;height:64px}

.counter-band{height:100px;background:var(--grey-dark)}
.counter-band .wrap{height:100px;display:flex;align-items:center;justify-content:space-between}
.digits{display:flex;gap:10px}
.digit{width:40px;height:52px;background:linear-gradient(#fff 50%,#e4e4e4 50%);border:2px solid #111;font-size:38px;font-weight:900;color:var(--ink);display:flex;align-items:center;justify-content:center}
.counter-text{text-align:right;color:#fff;text-transform:uppercase}
.counter-text strong{display:block;font-size:26px;font-weight:700}
.counter-text span{font-size:24px;font-weight:300}

/* promos */
.promos{display:flex;gap:13px;margin-top:22px;height:247px}
.locations{width:398px;background:var(--orange);padding:28px 25px}
.locations h2{font-size:33px;font-weight:500;color:var(--ink);margin-bottom:20px}
.store-search{height:70px;background:#fff;display:flex;align-items:center;gap:10px;padding:0 18px;font-size:13px;color:#999}
.map-btn{margin-top:18px;display:inline-block;background:var(--grey-dark);color:#fff;font-size:14px;padding:12px 26px}
.price-match{flex:1;background:linear-gradient(135deg,#3a3a3a,#151515);color:#fff;text-align:center;padding:34px 20px}
.price-match h2{font-size:28px;font-weight:700;text-transform:uppercase;letter-spacing:-.5px}
.price-match p{font-size:17px;color:#ccc;margin:10px 0}
.price-match h3{font-size:28px;font-weight:700}
.price-match small{display:block;font-size:13px;margin-top:18px}

/* features */
.features{display:flex;gap:10px;margin-top:20px}
.feature{width:213px;text-align:center}
.photo{height:143px}
.tone-a{background:linear-gradient(135deg,#5c6e7c,#2d3a45)}
.tone-b{background:linear-gradient(135deg,#8c8f96,#3c3f46)}
.tone-c{background:linear-gradient(135deg,#b36b3c,#4a2b1e)}
.tone-d{background:linear-gradient(135deg,#6f8679,#28362f)}
.feature h3{font-size:17px;font-weight:400;margin:34px 0 10px;min-height:22px;line-height:1.1}
.feature p{font-size:11px;color:#444;line-height:1.35;height:30px}
.read-more{display:inline-block;border:2px solid var(--orange);font-size:10px;font-weight:700;padding:8px 14px;margin-top:18px}

/* repair grid */
.band-title{height:71px;background:var(--grey-mid);color:#fff;display:flex;align-items:center;justify-content:center;font-size:34px;font-weight:700;margin-top:38px}
.repairs{height:500px;background:linear-gradient(180deg,#eceff1,#dfe3e6);position:relative}
.repair-grid{width:880px;margin:0 auto;display:grid;grid-template-columns:repeat(5,1fr);grid-template-rows:250px 250px}
.repair-cell{border-right:1px solid #c9cdd0;border-bottom:1px solid #c9cdd0;text-align:center;padding:24px 14px 0}
.repair-cell:nth-child(5n){border-right:none}
.repair-cell:nth-child(n+6){border-bottom:none}
.repair-cell svg{height:64px;width:64px}
.repair-cell h3{font-size:18px;font-weight:400;margin:14px 0 20px;line-height:1.2;min-height:44px}
.repair-cell p{font-size:9px;font-weight:700;line-height:1.4}

.action-band{height:91px;background:var(--orange);color:#fff}
.action-band .wrap{height:91px;display:flex;align-items:center;justify-content:space-between;width:920px}
.action{display:flex;align-items:center;gap:16px;font-size:18px;font-weight:500}

/* why choose */
.section-title{text-align:center;font-size:34px;font-weight:700;color:var(--black);letter-spacing:-.5px}
.why-title{margin-top:38px}
.why{display:flex;gap:10px;margin-top:36px}
.why-card{width:213px;height:253px;position:relative}
.why-card .photo{height:203px}
.why-card span{position:absolute;bottom:0;left:0;right:0;height:50px;background:#1d1d1d;color:#fff;font-size:13px;display:flex;align-items:center;justify-content:center}
.say-title{margin-top:36px}

/* testimonials */
.testimonials{height:397px;background:var(--grey-pale);margin-top:30px;position:relative}
.testimonials .wrap{display:flex;gap:10px;padding-top:30px}
.quote{width:213px}
.quote h3{color:var(--orange);font-size:19px;font-weight:500}
.tag{display:flex;align-items:center;gap:6px;font-size:11px;margin-top:10px}
.quote-box{background:#e9e9e9;margin-top:24px;padding:14px 12px;font-size:11px;line-height:1.3;color:#333;height:140px}
.quote-foot{display:flex;align-items:center;justify-content:space-between;margin-top:18px;font-size:13px;padding-left:12px}
.avatar{width:44px;height:44px;border-radius:50%;background:#d6c2ae;border:3px solid #fff}
.arrow{position:absolute;top:170px;width:12px;height:20px}

/* footer */
.footer{height:459px;background:linear-gradient(#222,#101010);color:#ccc;position:relative}
.footer-cols{display:flex;padding-top:32px}
.footer h4{color:#fff;font-size:18px;font-weight:400;margin-bottom:18px}
.info{width:233px}
.info li{list-style:none;font-size:12px;line-height:2}
.blog{width:443px}
.blog-post{display:flex;gap:14px;align-items:flex-start;margin-bottom:22px;position:relative}
.date{width:44px;height:44px;border-radius:50%;background:#fff;border:3px solid var(--orange);color:var(--orange);font-size:9px;text-align:center;display:flex;align-items:center;justify-content:center;line-height:1.1;flex:none}
.post{border:1px solid #666;padding:10px 12px;width:340px;font-size:11px;line-height:1.3}
.post b{display:block;color:#fff;font-size:13px;font-weight:400;margin-bottom:3px}
.post em{font-style:normal;display:block;margin-top:4px}
.newsletter{flex:1}
.email-field{height:42px;background:#ddd;color:#777;font-size:11px;display:flex;align-items:center;padding-left:14px}
.subscribe{display:inline-block;background:var(--orange);color:#fff;font-size:11px;font-weight:700;padding:8px 14px;margin-top:16px}
.socials{display:flex;gap:8px;margin-top:28px}
.socials i{width:22px;height:22px;border-radius:50%;border:1px solid #aaa;display:block}
.cant-find{color:#fff;font-size:20px;margin-top:8px}
.contacts{display:flex;justify-content:space-between;margin-top:40px}
.contact{display:flex;gap:12px;font-size:11px;line-height:1.5}
.contact strong{color:var(--orange);font-size:15px;font-weight:400;display:block}
.contact u{color:var(--orange)}
.bottom-bar{position:absolute;left:0;right:0;top:3265px;height:44px;background:var(--orange)}
.bottom-bar .wrap{height:44px;display:flex;align-items:center;justify-content:space-between}
.cards{display:flex;gap:5px}
.cards i{display:block;width:36px;height:22px;background:#fff;border-radius:2px}
.copyright{font-size:11px;color:#fff}
</style>
</head>
<body>

<div class="topbar">
  <div class="wrap">
    <div class="quick-links">QUICK LINKS <span>▾</span></div>
    <div class="top-right">
      <span class="lang">GRE <b>ENG</b></span>
      <i class="social-dot"></i><i class="social-dot"></i><i class="social-dot"></i><i class="social-dot"></i><i class="social-dot"></i><i class="social-dot"></i><i class="social-dot"></i>
    </div>
  </div>
</div>

<header class="header">
  <div class="wrap">
    <div class="brand"><span class="brand-mark"></span>Fixoloda</div>
    <nav class="nav"><a href="#">Repairs</a><a href="#">20 Stores</a><a href="#">Blog</a></nav>
    <div class="call">
      <span class="call-icon"><svg width="16" height="20" viewBox="0 0 16 20"><rect x="2" y="1" width="12" height="18" rx="2" fill="none" stroke="#222" stroke-width="2"/><circle cx="8" cy="15" r="1.3" fill="#222"/></svg></span>
      <div><small>Call to Us</small><strong>210 555 0142</strong></div>
    </div>
    <a class="chat-btn" href="#">ChatNow</a>
  </div>
</header>

<section class="hero" role="img" aria-label="Close-up video still of a phone circuit board being repaired">
  <svg class="play" viewBox="0 0 64 64"><circle cx="32" cy="32" r="29" fill="none" stroke="rgba(255,255,255,.7)" stroke-width="3"/><path d="M26 20 L45 32 L26 44Z" fill="rgba(255,255,255,.7)"/></svg>
</section>

<section class="counter-band">
  <div class="wrap">
    <div class="digits"><span class="digit">2</span><span class="digit">0</span><span class="digit">1</span><span class="digit">7</span></div>
    <div class="counter-text"><strong>Repairs complete with happy customers.</strong><span>Yep, we fix a lot of devices!</span></div>
  </div>
</section>

<div class="wrap">
  <div class="promos">
    <div class="locations">
      <h2>20 fixoloda Locations</h2>
      <div class="store-search"><svg width="12" height="16" viewBox="0 0 12 16"><path d="M6 0a6 6 0 0 1 6 6c0 4-6 10-6 10S0 10 0 6a6 6 0 0 1 6-6z" fill="#555"/><circle cx="6" cy="6" r="2" fill="#fff"/></svg>Find a store near You</div>
      <a class="map-btn" href="#">View Map</a>
    </div>
    <div class="price-match">
      <h2>Find a lower price for your</h2>
      <p>Fonix or Tabula repair?*</p>
      <h3>WE WILL MATCH IT!*</h3>
      <small>* Terms and conditions apply, click to read more</small>
    </div>
  </div>

  <div class="features">
    <div class="feature"><div class="photo tone-a" role="img" aria-label="Hands repairing a phone with a loupe"></div><h3>Open Service Area</h3><p>Repair right in front of you.<br>No closed doors, no back rooms.</p><a class="read-more" href="#">READ MORE</a></div>
    <div class="feature"><div class="photo tone-b" role="img" aria-label="Opened phone with parts on a workbench"></div><h3>Save 50-75% on multiple repairs</h3><p>If your device needs more than 1 part replaced, save up to 75% on extra parts.</p><a class="read-more" href="#">READ MORE</a></div>
    <div class="feature"><div class="photo tone-c" role="img" aria-label="Technician working on a device with tools"></div><h3>Accessories</h3><p>Lorem Ipsum is simply dummy text of the printing and typesetting industry.</p><a class="read-more" href="#">READ MORE</a></div>
    <div class="feature"><div class="photo tone-d" role="img" aria-label="Laptop motherboard under repair"></div><h3>20 minute repairs</h3><p>Most repairs can be completed in about 20 minutes.</p><a class="read-more" href="#">READ MORE</a></div>
  </div>
</div>

<h2 class="band-title">WHAT WE REPAIR?</h2>
<section class="repairs">
  <div class="repair-grid">
    <div class="repair-cell"><svg viewBox="0 0 64 64"><rect x="20" y="6" width="24" height="50" rx="4" fill="none" stroke="#111" stroke-width="3"/><circle cx="32" cy="50" r="2" fill="#111"/></svg><h3>Fonix Repair</h3><p>Lorem Ipsum is simply dummy text of the printing and typesetting industry.</p></div>
    <div class="repair-cell"><svg viewBox="0 0 64 64"><rect x="12" y="6" width="40" height="52" rx="4" fill="none" stroke="#111" stroke-width="3"/><rect x="17" y="11" width="30" height="40" fill="none" stroke="#111" stroke-width="1.5"/></svg><h3>Tabula Repair</h3><p>Lorem Ipsum is simply dummy text of the printing and typesetting industry.</p></div>
    <div class="repair-cell"><svg viewBox="0 0 64 64"><rect x="22" y="10" width="20" height="42" rx="3" fill="none" stroke="#111" stroke-width="3"/><circle cx="32" cy="46" r="2" fill="#111"/></svg><h3>Tunepod Touch Repair</h3><p>Lorem Ipsum is simply dummy text of the printing and typesetting industry.</p></div>
    <div class="repair-cell"><svg viewBox="0 0 64 64"><rect x="19" y="6" width="26" height="52" rx="5" fill="none" stroke="#111" stroke-width="3"/><line x1="19" y1="14" x2="45" y2="14" stroke="#111" stroke-width="1.5"/><line x1="19" y1="50" x2="45" y2="50" stroke="#111" stroke-width="1.5"/></svg><h3>Sorano Repair</h3><p>Lorem Ipsum is simply dummy text of the printing and typesetting industry.</p></div>
    <div class="repair-cell"><svg viewBox="0 0 64 64"><rect x="18" y="6" width="28" height="52" rx="4" fill="#111"/><rect x="22" y="10" width="20" height="16" fill="#fff"/><g fill="#fff"><rect x="22" y="32" width="5" height="4"/><rect x="30" y="32" width="5" height="4"/><rect x="38" y="32" width="4" height="4"/><rect x="22" y="40" width="5" height="4"/><rect x="30" y="40" width="5" height="4"/><rect x="38" y="40" width="4" height="4"/></g></svg><h3>Darkfruit Repair</h3><p>Lorem Ipsum is simply dummy text of the printing and typesetting industry.</p></div>
    <div class="repair-cell"><svg viewBox="0 0 64 64"><rect x="6" y="12" width="52" height="34" rx="2" fill="none" stroke="#111" stroke-width="3"/><path d="M26 46 L24 54 H40 L38 46" fill="none" stroke="#111" stroke-width="3"/></svg><h3>Desko Repairs</h3><p>Lorem Ipsum is simply dummy text of the printing and typesetting industry.</p></div>
    <div class="repair-cell"><svg viewBox="0 0 64 64"><rect x="12" y="14" width="40" height="28" rx="2" fill="none" stroke="#111" stroke-width="3"/><path d="M4 46 H60 L56 50 H8Z" fill="#111"/></svg><h3>Notia Book Repair</h3><p>Lorem Ipsum is simply dummy text of the printing and typesetting industry.</p></div>
    <div class="repair-cell"><svg viewBox="0 0 64 64"><rect x="4" y="14" width="38" height="28" fill="none" stroke="#111" stroke-width="3"/><rect x="18" y="42" width="10" height="6" fill="#111"/><rect x="46" y="10" width="14" height="40" fill="#111"/></svg><h3>Computer Repair</h3><p>Lorem Ipsum is simply dummy text of the printing and typesetting industry.</p></div>
    <div class="repair-cell"><svg viewBox="0 0 64 64"><rect x="12" y="14" width="40" height="28" fill="none" stroke="#111" stroke-width="3"/><path d="M6 46 H58 V50 H6Z" fill="#111"/></svg><h3>Laptop Repair</h3><p>Lorem Ipsum is simply dummy text of the printing and typesetting industry.</p></div>
    <div class="repair-cell"><svg viewBox="0 0 64 64"><path d="M32 14a14 14 0 0 1 8 25v6H24v-6a14 14 0 0 1 8-25z" fill="none" stroke="#111" stroke-width="3"/><rect x="25" y="48" width="14" height="5" fill="#111"/><path d="M26 28l5 5 8-8" fill="none" stroke="#111" stroke-width="3"/><g stroke="#111" stroke-width="3"><line x1="32" y1="4" x2="32" y2="9"/><line x1="12" y1="12" x2="16" y2="16"/><line x1="52" y1="12" x2="48" y2="16"/></g></svg><h3>Business Services</h3><p>Lorem Ipsum is simply dummy text of the printing and typesetting industry.</p></div>
  </div>
</section>

<section class="action-band">
  <div class="wrap">
    <div class="action"><svg width="64" height="44" viewBox="0 0 64 44"><path d="M2 6h36v26H2z M38 14h14l10 10v8H38z" fill="#fff"/><circle cx="14" cy="36" r="6" fill="#fff" stroke="#f7901e" stroke-width="2"/><circle cx="50" cy="36" r="6" fill="#fff" stroke="#f7901e" stroke-width="2"/></svg>Find A store near you?</div>
    <div class="action"><svg width="46" height="50" viewBox="0 0 46 50"><path d="M8 14h30l4 34H4z" fill="#fff"/><path d="M15 16V10a8 8 0 0 1 16 0v6" fill="none" stroke="#fff" stroke-width="3"/></svg>Send us your device</div>
    <div class="action"><svg width="50" height="50" viewBox="0 0 50 50"><circle cx="25" cy="25" r="24" fill="#fff"/><text x="25" y="34" text-anchor="middle" font-size="28" font-weight="700" fill="#f7901e" font-family="Roboto,sans-serif">$</text></svg>Free pickup in Athens</div>
  </div>
</section>

<h2 class="section-title why-title">WHY CHOOSE FIXOLODA?</h2>
<div class="wrap">
  <div class="why">
    <div class="why-card"><div class="photo tone-d" role="img" aria-label="Cracked phone screen being replaced"></div><span>Open Service Area</span></div>
    <div class="why-card"><div class="photo tone-b" role="img" aria-label="Technician soldering a phone board"></div><span>Save 50-75% on multiple repairs</span></div>
    <div class="why-card"><div class="photo tone-a" role="img" aria-label="Repair specialist working at a desk"></div><span>Accessories</span></div>
    <div class="why-card"><div class="photo tone-d" role="img" aria-label="Gloved hands opening a phone"></div><span>20 minute repairs</span></div>
  </div>
</div>

<h2 class="section-title say-title">WHAT OUR CUSTOMER SAYING</h2>
<section class="testimonials">
  <svg class="arrow" style="left:130px" viewBox="0 0 12 20"><path d="M10 2 L2 10 L10 18" fill="none" stroke="#555" stroke-width="2"/></svg>
  <svg class="arrow" style="right:130px" viewBox="0 0 12 20"><path d="M2 2 L10 10 L2 18" fill="none" stroke="#555" stroke-width="2"/></svg>
  <div class="wrap">
    <div class="quote"><h3>Laptop Repair</h3><div class="tag"><svg width="14" height="14" viewBox="0 0 14 14"><circle cx="7" cy="7" r="7" fill="#f7901e"/><path d="M4 7l2 2 4-4" fill="none" stroke="#fff" stroke-width="1.8"/></svg>Overheating</div><div class="quote-box">Lorem Ipsum is simply dummy text of the printing and typesetting industry. Lorem Ipsum has been the industry's standard dummy text ever since the 1500s, when an unknown printer took a galley of type and scrambled it to make a type specimen book. It has survived not only five centuries, but also the leap into electronic typesetting, remaining essentially unchanged.</div><div class="quote-foot">Eleni P.Marousi<span class="avatar" role="img" aria-label="Customer portrait"></span></div></div>
    <div class="quote"><h3>Laptop Repair</h3><div class="tag"><svg width="14" height="14" viewBox="0 0 14 14"><circle cx="7" cy="7" r="7" fill="#f7901e"/><path d="M4 7l2 2 4-4" fill="none" stroke="#fff" stroke-width="1.8"/></svg>Overheating</div><div class="quote-box">Lorem Ipsum is simply dummy text of the printing and typesetting industry. Lorem Ipsum has been the industry's standard dummy text ever since the 1500s, when an unknown printer took a galley of type and scrambled it to make a type specimen book. It has survived not only five centuries, but also the leap into electronic typesetting, remaining essentially unchanged.</div><div class="quote-foot">Eleni P.Marousi<span class="avatar" role="img" aria-label="Customer portrait"></span></div></div>
    <div class="quote"><h3>Laptop Repair</h3><div class="tag"><svg width="14" height="14" viewBox="0 0 14 14"><circle cx="7" cy="7" r="7" fill="#f7901e"/><path d="M4 7l2 2 4-4" fill="none" stroke="#fff" stroke-width="1.8"/></svg>Overheating</div><div class="quote-box">Lorem Ipsum is simply dummy text of the printing and typesetting industry. Lorem Ipsum has been the industry's standard dummy text ever since the 1500s, when an unknown printer took a galley of type and scrambled it to make a type specimen book. It has survived not only five centuries, but also the leap into electronic typesetting, remaining essentially unchanged.</div><div class="quote-foot">Eleni P.Marousi<span class="avatar" role="img" aria-label="Customer portrait"></span></div></div>
    <div class="quote"><h3>Laptop Repair</h3><div class="tag"><svg width="14" height="14" viewBox="0 0 14 14"><circle cx="7" cy="7" r="7" fill="#f7901e"/><path d="M4 7l2 2 4-4" fill="none" stroke="#fff" stroke-width="1.8"/></svg>Overheating</div><div class="quote-box">Lorem Ipsum is simply dummy text of the printing and typesetting industry. Lorem Ipsum has been the industry's standard dummy text ever since the 1500s, when an unknown printer took a galley of type and scrambled it to make a type specimen book. It has survived not only five centuries, but also the leap into electronic typesetting, remaining essentially unchanged.</div><div class="quote-foot">Eleni P.Marousi<span class="avatar" role="img" aria-label="Customer portrait"></span></div></div>
  </div>
</section>

<footer class="footer">
  <div class="wrap">
    <div class="footer-cols">
      <div class="info"><h4>Information</h4><ul><li>» Repairs</li><li>» 20 Stores</li><li>» Blog</li></ul></div>
      <div class="blog"><h4>Fixoloda Blog</h4>
        <div class="blog-post"><span class="date">05/03<br>2017</span><div class="post"><b>Lorem Ipsum is simply dummy text...</b>Lorem Ipsum is simply dummy text of the printing and typesetting industry. Lorem Ipsum has been the industry's...<em>Read More...</em></div></div>
        <div class="blog-post"><span class="date">05/03<br>2017</span><div class="post"><b>Lorem Ipsum is simply dummy text...</b>Lorem Ipsum is simply dummy text of the printing and typesetting industry. Lorem Ipsum has been the industry's...<em>Read More...</em></div></div>
      </div>
      <div class="newsletter"><h4>Newsletter</h4><div class="email-field">Enter Your Email Id</div><a class="subscribe" href="#">SUBSCRIBE</a><div class="socials"><i></i><i></i><i></i><i></i><i></i></div></div>
    </div>
    <p class="cant-find">Can't find what you need?</p>
    <div class="contacts">
      <div class="contact"><svg width="22" height="16" viewBox="0 0 22 16"><rect x="1" y="1" width="20" height="14" fill="none" stroke="#fff" stroke-width="2"/><path d="M1 1l10 8 10-8" fill="none" stroke="#fff" stroke-width="2"/></svg><div><strong>Email Support</strong>We usually responsed within 24 hours<br><u>Click to send email</u></div></div>
      <div class="contact"><svg width="20" height="20" viewBox="0 0 20 20"><path d="M4 1l4 4-2 3c1 3 3 5 6 6l3-2 4 4-3 3C8 19 1 12 1 4z" fill="none" stroke="#fff" stroke-width="1.8"/></svg><div><strong>Contact our call center</strong>Call to speak to a customer service rep.<br><u>210 555 0142</u></div></div>
      <div class="contact"><svg width="22" height="20" viewBox="0 0 22 20"><path d="M2 2h14v10H8l-4 4v-4H2z" fill="none" stroke="#fff" stroke-width="1.8"/><path d="M18 6h2v10h-2v3l-3-3h-5" fill="none" stroke="#fff" stroke-width="1.8"/></svg><div><strong>Live chat</strong>Chat with an Fixoloda technician now.<br><u>Click to chat</u></div></div>
    </div>
  </div>
</footer>

<div class="bottom-bar">
  <div class="wrap">
    <div class="cards"><i></i><i></i><i></i><i></i></div>
    <span class="copyright">Copyright 2017. All Right Reserved.</span>
  </div>
</div>

</body>
</html>
```